EXTENDED Store hours to serve your healthcare needs

I'M LOOKING FOR A NICE FLYER THAT SHOWS THE FOLLOWING INFORMATION:

Logo
address
tel phone and fax
email address

Extending our hours to meet the growing healthcare needs of our community. Fast delivery service!

Monday - Thursday 10am-midnight
Friday 10am-4pm
Saturday - Motzei Shabbos till midnight
Sunday 10am-7pm

Target Market(s)

Community

Industry/Entity Type

Pharmacy

Requirements
Must have
• Extended hours
• personal care
• expert advice
• superior service
Nice to have
• Looking for no people pictures
• Eye popping design
• Classic modern clean design
Should not have
• store description is services
• And should not say Fiirst to open and last to close

```html
<!DOCTYPE html>
<html lang="en">
<head>
<meta charset="utf-8">
<title>Lindell Pharmacy – Extended Hours Flyer</title>
<link href="https://fonts.googleapis.com/css2?family=Open+Sans:wght@400;600;700&display=swap" rel="stylesheet">
<style>
  :root {
    --navy: #2b3490;
    --sky: #0a9ad9;
    --cyan: #0aa3e6;
    --red: #e0202b;
    --wine: #a8283a;
    --white: #ffffff;
    --page: #eceae6;
  }
  * { box-sizing: border-box; margin: 0; padding: 0; }
  html, body { width: 1200px; height: 1200px; overflow: hidden; }
  body {
    background: var(--page);
    font-family: "Open Sans", Arial, sans-serif;
    position: relative;
  }
  .flyer {
    position: absolute;
    left: 328px; top: 30px;
    width: 543px; height: 1140px;
    background: var(--white);
    overflow: hidden;
    box-shadow: 0 6px 20px rgba(0,0,0,0.18);
  }
  .hero { position: absolute; left: 0; top: 0; width: 543px; height: 437px; display: block; }
  .brand {
    position: absolute; left: 0; top: 478px; width: 543px;
    display: flex; align-items: center; justify-content: center; gap: 14px;
  }
  .brand-mark { width: 22px; height: 22px; border-radius: 50%; background: var(--navy); }
  .brand-name {
    font-size: 40px; font-weight: 600; color: var(--navy);
    letter-spacing: 1px; line-height: 1;
  }
  .services {
    position: absolute; left: 0; top: 548px; width: 543px;
    text-align: center; color: var(--navy);
    font-size: 15px; font-weight: 600; letter-spacing: 2px;
    text-transform: uppercase; line-height: 20px;
  }
  .promo {
    position: absolute; left: 32px; top: 619px; width: 479px; height: 67px;
    border-radius: 34px;
    background: linear-gradient(90deg, var(--navy) 0%, var(--cyan) 50%, var(--navy) 100%);
    box-shadow: 3px 3px 0 #1d1d3a;
    color: var(--white);
    font-weight: 700; font-size: 21px; letter-spacing: 0.3px;
    display: flex; align-items: center; justify-content: center;
  }
  .tagline {
    position: absolute; left: 0; top: 732px; width: 543px;
    text-align: center; color: var(--sky);
    font-size: 27px; line-height: 30px;
  }
  .hours {
    position: absolute; left: 0; top: 843px; width: 543px;
    text-align: center; color: var(--sky);
    font-size: 21px; line-height: 25.6px;
  }
  .hours h2 { color: var(--red); font-size: 22px; font-weight: 700; line-height: 26px; }
  .band {
    position: absolute; left: 0; top: 978px; width: 543px; height: 15px;
    background: linear-gradient(90deg, var(--navy) 0%, var(--cyan) 50%, var(--navy) 100%);
  }
  .contact {
    position: absolute; left: 0; top: 993px; width: 543px; height: 147px;
    background: linear-gradient(90deg, var(--wine) 0%, var(--red) 50%, var(--wine) 100%);
    color: var(--white); text-align: center;
    font-size: 21px; line-height: 26px;
    padding-top: 30px;
  }
  .contact strong { font-weight: 700; }
</style>
</head>
<body>
  <main class="flyer">
    <svg class="hero" viewBox="0 0 645 520" preserveAspectRatio="none">
      <defs>
        <linearGradient id="photoTone" x1="0" y1="0" x2="1" y2="1">
          <stop offset="0" stop-color="#f1efed"/>
          <stop offset="0.35" stop-color="#e6d3c6"/>
          <stop offset="0.7" stop-color="#eeeeee"/>
          <stop offset="1" stop-color="#f2e9a8"/>
        </linearGradient>
        <linearGradient id="waveLine" x1="0" y1="0" x2="1" y2="0">
          <stop offset="0" stop-color="#2b3490"/>
          <stop offset="0.6" stop-color="#2b3490"/>
          <stop offset="0.85" stop-color="#0aa3e6"/>
          <stop offset="1" stop-color="#2b3490"/>
        </linearGradient>
      </defs>
      <rect class="hero-photo" role="img" aria-label="Photo of a pharmacist's hands opening a prescription bottle at a counter" x="0" y="0" width="645" height="520" fill="url(#photoTone)"/>
      <path class="hero-wave" d="M0 415 C 110 370, 230 380, 360 440 S 560 525, 645 490 L645 520 L0 520 Z" fill="#ffffff"/>
      <path class="hero-wave-line" d="M0 415 C 110 370, 230 380, 360 440 S 560 525, 645 490" fill="none" stroke="url(#waveLine)" stroke-width="9"/>
    </svg>

    <div class="brand">
      <span class="brand-mark"></span>
      <span class="brand-name">Lindell Pharmacy</span>
    </div>

    <p class="services">Personal Care · Expert Advice · Superior Service</p>

    <div class="promo">FAST DELIVERY SERVICE!</div>

    <p class="tagline">Extending our hours to meet<br>the growing healthcare needs<br>of our community.</p>

    <section class="hours">
      <h2>Hours of Operation</h2>
      <p>Monday - Thursday 10am - midnight</p>
      <p>Friday 10am - 4pm</p>
      <p>Saturday - Motzei Shabbos till midnight</p>
      <p>Sunday 10am-7pm</p>
    </section>

    <div class="band"></div>

    <footer class="contact">
      <p><strong>482 Maple Ave., Brooklyn, NY 11200</strong></p>
      <p>Phone <strong>555-014-2280</strong> <strong>|</strong> Fax <strong>555-014-2291</strong></p>
      <p>Email <strong>lindellpharmacy@example.com</strong></p>
    </footer>
  </main>
</body>
</html>
```